Roll Up Design Velumo

We are a beauty company and we need stunning design for our general roll-up banner that we gonna place just next to the main gate of mall that we are located in. The most important for us is the quality, accuracy and the unity of poster. It has to be super elegant, engaging and beautiful. Has to match our service standards (high). Colors do not matter as long as the overall look is exciting.
Examples and our logo are attached
Updates
Reason: We need more designs (more creativity, more quality, colurs and proportions).
Target Market(s)
Middle class ladies, students, business women
Industry/Entity Type
It Company
Colors
Designer to choose colors to be used in the design.
Look and feel
Each slider illustrates characteristics of the customer's brand and the style your logo design should communicate.

```html
<!DOCTYPE html>
<html lang="en">
<head>
<meta charset="utf-8">
<title>Velumo Gözəllik – Roll-up Banner</title>
<link href="https://fonts.googleapis.com/css2?family=Questrial&display=swap" rel="stylesheet">
<style>
  :root {
    --ink: #1c1c1c;
    --gold: #a57a2c;
    --gold-light: #ead79e;
    --gold-deep: #c39a45;
    --night: #05070c;
    --slate: #3b4656;
    --paper: #ffffff;
    --paper-fade: #e6e6e6;
    --rule: #8a8a8a;
  }
  html, body {
    margin: 0;
    padding: 0;
    overflow: hidden;
    background: #ffffff;
  }
  .banner {
    position: relative;
    width: 1200px;
    height: 2880px;
    overflow: hidden;
    font-family: "Questrial", "Century Gothic", sans-serif;
    background: var(--paper);
  }
  .banner__art {
    position: absolute;
    inset: 0;
    width: 1200px;
    height: 2880px;
  }
  .services {
    position: absolute;
    left: 436px;
    top: 1530px;
    margin: 0;
    padding: 0;
    list-style: none;
  }
  .services__item {
    display: flex;
    align-items: center;
    height: 132px;
    font-size: 76px;
    color: var(--gold);
    letter-spacing: 0.5px;
  }
  .services__marker {
    width: 42px;
    height: 42px;
    margin-right: 38px;
    flex: none;
  }
  .brand {
    position: absolute;
    left: 0;
    top: 2236px;
    width: 1200px;
    text-align: center;
  }
  .brand__name {
    font-size: 150px;
    line-height: 1;
    letter-spacing: 14px;
    color: var(--ink);
    text-transform: uppercase;
  }
  .brand__rule {
    width: 516px;
    height: 2px;
    margin: 38px auto 30px;
    background: var(--rule);
  }
  .brand__tagline {
    font-size: 56px;
    letter-spacing: 4px;
    color: var(--ink);
  }
  .shop {
    position: absolute;
    left: 0;
    top: 2692px;
    width: 1200px;
    text-align: center;
    color: var(--gold);
    line-height: 1;
  }
  .shop__label {
    font-size: 60px;
  }
  .shop__number {
    font-size: 112px;
    letter-spacing: 5px;
    margin-left: 22px;
  }
</style>
</head>
<body>
<main class="banner">
  <svg class="banner__art" viewBox="0 0 1200 2880" xmlns="http://www.w3.org/2000/svg">
    <defs>
      <radialGradient id="backdropTone" cx="0.5" cy="0.3" r="0.8">
        <stop offset="0" stop-color="#3f4a5a"/>
        <stop offset="0.5" stop-color="#1a212c"/>
        <stop offset="1" stop-color="#04060a"/>
      </radialGradient>
      <radialGradient id="hairTone" cx="0.5" cy="0.35" r="0.6">
        <stop offset="0" stop-color="#2a3038"/>
        <stop offset="0.7" stop-color="#111419"/>
        <stop offset="1" stop-color="#111419" stop-opacity="0"/>
      </radialGradient>
      <radialGradient id="skinTone" cx="0.5" cy="0.5" r="0.5">
        <stop offset="0" stop-color="#e9b9a3"/>
        <stop offset="0.6" stop-color="#c98d78"/>
        <stop offset="1" stop-color="#c98d78" stop-opacity="0"/>
      </radialGradient>
      <linearGradient id="goldBand" x1="0" y1="0" x2="1" y2="0">
        <stop offset="0" stop-color="#c39a45"/>
        <stop offset="0.5" stop-color="#ead79e"/>
        <stop offset="1" stop-color="#d3b468"/>
      </linearGradient>
      <linearGradient id="paperFill" x1="0" y1="0" x2="0" y2="1">
        <stop offset="0" stop-color="#ffffff"/>
        <stop offset="0.55" stop-color="#ffffff"/>
        <stop offset="1" stop-color="#e6e6e6"/>
      </linearGradient>
    </defs>
    <g class="banner__portrait" role="img" aria-label="Portrait photo of a woman with long, glossy straight black hair and a full fringe on a dark background">
      <rect x="0" y="0" width="1200" height="1560" fill="url(#backdropTone)"/>
      <ellipse cx="600" cy="820" rx="560" ry="760" fill="url(#hairTone)"/>
      <ellipse cx="600" cy="720" rx="230" ry="330" fill="url(#skinTone)" opacity="0.85"/>
      <ellipse cx="600" cy="1130" rx="560" ry="150" fill="url(#skinTone)" opacity="0.45"/>
    </g>
    <path class="banner__wave-gold" d="M0,1405 C300,1440 600,1385 800,1275 C950,1192 1090,1138 1200,1126 L1200,2880 L0,2880 Z" fill="url(#goldBand)"/>
    <path class="banner__wave-paper" d="M0,1450 C300,1482 620,1425 820,1318 C970,1238 1100,1182 1200,1170 L1200,2880 L0,2880 Z" fill="url(#paperFill)"/>
  </svg>

  <ul class="services">
    <li class="services__item"><svg class="services__marker" viewBox="0 0 10 10"><path d="M10,0 L10,10 L0,5 Z" fill="#a57a2c"/></svg>Beauty Treatment</li>
    <li class="services__item"><svg class="services__marker" viewBox="0 0 10 10"><path d="M10,0 L10,10 L0,5 Z" fill="#a57a2c"/></svg>Cosmetics</li>
    <li class="services__item"><svg class="services__marker" viewBox="0 0 10 10"><path d="M10,0 L10,10 L0,5 Z" fill="#a57a2c"/></svg>Hair Art</li>
    <li class="services__item"><svg class="services__marker" viewBox="0 0 10 10"><path d="M10,0 L10,10 L0,5 Z" fill="#a57a2c"/></svg>Nail Art</li>
  </ul>

  <div class="brand">
    <div class="brand__name">Velumo</div>
    <div class="brand__rule"></div>
    <div class="brand__tagline">GÖZƏLLİK</div>
  </div>

  <div class="shop">
    <span class="shop__label">Shop No:</span><span class="shop__number">B-417</span>
  </div>
</main>
</body>
</html>
```